Nimbora.com based Professional Services organization needs a stellar marketing flyer.

We need a marketing flyer for a new company (refer to website www.kavrel.com) that specializes in professional services for businesses in financial services that have or are implementing cloud based systems like nimbora.com.

We aim to re-engineer their process for improved efficiency & productivity, enhance transparency throughout the organization, maximize user adoption rates, ensure compliance, and reduce operating costs.

Our website contains more information about our specific approach and services we offer. Please refer to the site for that information and match the colors that are included in the attached logo.

Typical clients are those that are interested in engaging in some level of business process re-engineering, implementing new cloud-based software (mostly nimbora.com), need additional features or customization to existing nimbora.com platforms, or need end-user training, documentation, or reinforcement.

Also attached are a few files from an internal stab at a marketing flyer.

Target Market(s)

Financial services industry (credit unions, community banks, insurance finance companies, wealth management, private equity)

Generally this market is reluctant to join the cloud revolution. We aim to re-engineer their process for improved efficiency & productivity, enhance transparency throughout the organization, maximize user adoption rates, ensure compliance, and reduce operating costs.

Industry/Entity Type

Marketing

Requirements
Must have
• Must include the nimbora.com logo and the kavrel logo that is attached.
Color scheme must also coordinate with the logo colors.

```html
<!DOCTYPE html>
<html lang="en">
<head>
<meta charset="utf-8">
<title>Kavrel – Our Approach</title>
<link rel="stylesheet" href="https://fonts.googleapis.com/css2?family=Arimo:wght@400;700&display=swap">
<style>
  :root{
    --navy:#0f3d57;
    --orange:#f07020;
    --sky:#5bb8e4;
    --mist:#d2d3d5;
    --card:#e9edf1;
    --ink:#1e1e1e;
    --page:#eef0f2;
    --white:#ffffff;
  }
  *{box-sizing:border-box;margin:0;padding:0}
  html,body{width:1171px;height:1200px;overflow:hidden;background:var(--page)}
  body{font-family:"Arimo",Arial,sans-serif;color:var(--ink)}
  .flyer{position:absolute;left:145px;top:30px;width:880px;height:1140px;overflow:hidden;
    background:linear-gradient(160deg,#ffffff 0%,#eef1f4 22%,#ffffff 40%,#ffffff 100%);
    box-shadow:0 4px 18px rgba(0,0,0,.15)}
  .flyer-title{position:absolute;left:51px;top:52px;font-size:33px;font-weight:700;color:var(--navy)}
  .flyer-title span{color:var(--orange)}
  .step{position:absolute;width:271px;background:linear-gradient(180deg,rgba(233,237,241,.55),var(--card));
    border-radius:14px;text-align:center}
  .step-icon{position:absolute;left:50%;width:90px;height:90px;margin-left:-45px;border-radius:50%;
    background:var(--navy);display:flex;align-items:center;justify-content:center}
  .step-icon svg{width:50px;height:50px}
  .step-name{position:absolute;left:0;right:0;font-size:21px;font-weight:700;color:var(--orange)}
  .step-text{position:absolute;left:14px;right:14px;font-size:14.5px;line-height:1.3}
  .row-one{top:171px;height:251px}
  .row-two{top:473px;height:235px}
  .row-one .step-name{top:44px}.row-one .step-text{top:82px}
  .row-two .step-name{top:52px}.row-two .step-text{top:92px}
  .focus-title{position:absolute;left:598px;top:466px;font-size:37px;font-weight:400;line-height:48px;color:var(--navy)}
  .device-art{position:absolute;left:716px;top:460px;width:158px;height:160px;border-radius:6px;
    background:linear-gradient(180deg,#c9dbe9 0%,#8eb6d4 55%,#e2c6ad 100%)}
  .list-box{position:absolute;top:729px;height:362px;padding:26px 24px}
  .list-box h2{font-size:31px;font-weight:400;line-height:1.1;margin-bottom:24px}
  .list-box ul{list-style:none}
  .list-box li{position:relative;padding-left:20px;font-size:15px;line-height:26px}
  .list-box li::before{content:"";position:absolute;left:0;top:9px;width:9px;height:9px;border-radius:50%;background:var(--navy)}
  .services{left:22px;width:274px;background:var(--sky);color:var(--white)}
  .services li{color:var(--navy)}
  .industries{left:300px;width:275px;background:var(--mist);color:var(--navy)}
  .industries li{font-size:14px;color:var(--ink)}
  .footer-bar{position:absolute;left:0;right:0;top:1091px;height:49px;background:var(--navy);
    color:var(--white);font-size:24px;padding:10px 0 0 43px;word-spacing:4px}
  .footer-bar span{margin-left:18px}
  .focus-panel{position:absolute;left:579px;top:615px;width:302px;height:498px}
  .focus-panel svg{position:absolute;inset:0}
  .focus-copy{position:absolute;left:22px;right:14px;top:40px;color:var(--white)}
  .focus-copy h3{font-size:25.5px;font-weight:700;line-height:1.2}
  .focus-copy p{font-size:15.4px;line-height:1.34}
</style>
</head>
<body>
<main class="flyer">
  <h1 class="flyer-title">Our <span>Approach</span></h1>

  <section class="step row-one" style="left:26px">
    <div class="step-icon" style="top:-58px">
      <svg viewBox="0 0 50 50" fill="none" stroke="#fff" stroke-width="5" stroke-linecap="round"><circle cx="29" cy="20" r="12"/><line x1="20" y1="29" x2="8" y2="42"/></svg>
    </div>
    <h2 class="step-name">Discovery</h2>
    <p class="step-text">We conduct an Operational Analysis of your business that leads to the development of our project plan and determines key factors of success.</p>
  </section>
  <section class="step row-one" style="left:300px">
    <div class="step-icon" style="top:-58px">
      <svg viewBox="0 0 50 50" fill="none" stroke="#fff" stroke-width="5" stroke-linecap="round"><line x1="12" y1="12" x2="38" y2="38"/><path d="M38 12 12 38"/><circle cx="38" cy="12" r="5"/><path d="M8 8l5 0 0 5"/></svg>
    </div>
    <h2 class="step-name">Integration</h2>
    <p class="step-text">The project timeline, scope and responsibilities are approved. This step involves software customization, process documentation, 3rd party integration and identification of training needs.</p>
  </section>
  <section class="step row-one" style="left:576px">
    <div class="step-icon" style="top:-58px">
      <svg viewBox="0 0 50 50" fill="none" stroke="#fff" stroke-width="4.5" stroke-linecap="round" stroke-linejoin="round"><path d="M8 18h32l-7-7"/><path d="M42 32H10l7 7"/></svg>
    </div>
    <h2 class="step-name">Transition</h2>
    <p class="step-text">We fully transition existing data and processes to Nimbora.com. A key component of our services involves training and managing software utilization with minimal disruptions to your day-to-day operations.</p>
  </section>

  <section class="step row-two" style="left:26px">
    <div class="step-icon" style="top:-58px">
      <svg viewBox="0 0 50 50" fill="none" stroke="#fff" stroke-width="5" stroke-linecap="round"><path d="M22 18l5-5a7 7 0 0 1 10 10l-5 5"/><path d="M28 32l-5 5a7 7 0 0 1-10-10l5-5"/><line x1="20" y1="30" x2="30" y2="20"/></svg>
    </div>
    <h2 class="step-name">Reinforcement</h2>
    <p class="step-text">For 90 days post-transition, our team monitors user adoption and compliance, provides training as needed, and gives feedback to key stakeholders.</p>
  </section>
  <section class="step row-two" style="left:300px">
    <div class="step-icon" style="top:-58px">
      <svg viewBox="0 0 50 50" fill="#fff" stroke="#fff" stroke-width="3" stroke-linecap="round"><path d="M6 24a19 15 0 0 1 38 0z"/><path d="M25 24v14a4 4 0 0 1-8 0" fill="none"/></svg>
    </div>
    <h2 class="step-name">Ongoing Support</h2>
    <p class="step-text">As you utilize the new system, your team may need additional software customizations, software maintenance, quality assurance monitoring or training.</p>
  </section>

  <h2 class="focus-title">We<br>Focus<br>On</h2>
  <div class="device-art" role="img" aria-label="Photo of a hand holding a laptop showing a cloud process diagram"></div>

  <section class="list-box services">
    <h2>What<br>We Do</h2>
    <ul>
      <li>Project Management</li><li>Software Development</li><li>Process Improvement</li><li>Implementation</li>
      <li>Customization</li><li>Training</li><li>User Adoption</li><li>Staff Augmentation</li>
    </ul>
  </section>
  <section class="list-box industries">
    <h2>Industries<br>Served</h2>
    <ul>
      <li>Banking</li><li>Trading</li><li>Insurance</li><li>Private Equity Firms</li><li>Wealth Management</li>
    </ul>
  </section>

  <footer class="footer-bar">888-KAVREL5<span>www.kavrel.com</span></footer>

  <aside class="focus-panel">
    <svg viewBox="0 0 302 498" preserveAspectRatio="none"><path d="M0 28Q150-12 302 8V498H0Z" fill="#f07020"/></svg>
    <div class="focus-copy">
      <h3>business process improvements -</h3>
      <p>we want to install software that accomplishes your long-term objectives, automates your manual processes, and leads to ongoing performance, efficiency, and cost gains and the user adoption piece Proper documentation, training, and monitoring will reinforce how to use the new system and reveal any gaps that require additional support. Our developers can customize the platform, monitor quality assurance, provide data back-up and security, and support your staff throughout the implementation process.</p>
    </div>
  </aside>
</main>
</body>
</html>
```